Form Crafters Business Card

Professional cosmetic surgery company, based in very exclusive area in London. High profiled clientele. Brand is very artistic, modern, state-of-the-art, safe. The best in the business. Celebrity clientele.

Form Crafter’s of London is a brand serving a discriminating and exclusive clientele who value personal service that is both intimate and high end. Our clients choose Form Crafters because of the relationships we share with all of our customers. The clients of Form Crafters have an equal partnership between customers, and very experienced, highly qualified medical professionals. This together provides you with a professional service that keeps you looking good and feeling good. It is a relationship based on honesty, compassion, loyalty and respect.
Form Crafter’s have provided services for internationally recognised celebrities, and other high profiled individuals.

The cards are used for networking at private, exclusive events with VIPs.

Target Market(s)

Professionals
Rich people

Industry/Entity Type

Professional Service

Contact Information for Business Card

Need double sided business card design for 4 people. Back of the business card needs to have contrast background to the front with butterfly watermark with services provided:
Hair Restoration surgery
Hair Loss treatments
Breast surgery
Rhinoplasty
Zelix Liposuction
Fat Grafting
Lumex & Fillers

Front of the business card needs to be a nice satin black.
with following information:
Talvan Desoruthy - name
Chief Executive - Job title

www.formcrafters-example.co.uk
talvan@formcrafters-example.co.uk
Phone: +44 (0)207 146 5327
Mobile: +44 (0)7491 825 436

The London Calder Infirmary
14 Pellmont Street | London | W1K 3TR
Off Dunmore Lane

All business cards have the same address, phone, website as Talvan's details.
Same details on the back of the business card as well.
The other cards have different name, job title, email, mobile number

Kerem Lutz - Name
Partner - Job Title
Former England International Cricketer - please include below job title

email: kerem@formcrafters-example.co.uk
mobile: +44(0)7862 514208

Dr Stellan Vastrel - Name
Plastic Surgeon - Job Title
drvastrel@formcrafters-example.co.uk
No mobile number

Dr Jon Torvick FRCS (please put FRCS in small font) - Name
Hair Restoration Surgeon - Job Title
drtorvick@formcrafters-example.co.uk
No mobile number

Colors
cedeec
85abd2
0655a3

Requirements
Must have
• The logo needs to be in a metallic finish
• Text needs to be striking
• nice background
• butterfly watermark on the back

```html
<!DOCTYPE html>
<html lang="en">
<head>
<meta charset="utf-8">
<title>Form Crafters Business Card</title>
<link href="https://fonts.googleapis.com/css2?family=Marcellus&family=Noticia+Text:ital,wght@0,400;0,700;1,400&display=swap" rel="stylesheet">
<style>
  :root {
    --page-bg: #d9d9d9;
    --satin-black: #0b0b0b;
    --card-white: #f4f4f4;
    --brand-blue: #1b78c8;
    --contact-blue: #1a68c0;
    --accent-orange: #ec7a22;
    --service-green: #6cb52c;
    --divider: #222222;
  }
  * { box-sizing: border-box; margin: 0; padding: 0; }
  html, body {
    width: 1200px;
    height: 1000px;
    overflow: hidden;
    background: var(--page-bg);
  }
  .sheet {
    position: relative;
    width: 1200px;
    height: 1000px;
  }
  .card {
    position: absolute;
    left: 280px;
    width: 640px;
    height: 366px;
    box-shadow: 0 6px 18px rgba(0,0,0,0.18);
  }

  /* Front */
  .card-front {
    top: 92px;
    background: radial-gradient(ellipse at 40% 35%, #1a1a1a 0%, var(--satin-black) 70%);
  }
  .brand {
    position: absolute;
    left: 90px;
    top: 92px;
    display: flex;
    align-items: center;
    gap: 16px;
  }
  .brand-mark {
    width: 26px;
    height: 26px;
    border-radius: 50%;
    background: var(--accent-orange);
  }
  .brand-name {
    font-family: "Marcellus", serif;
    font-size: 54px;
    letter-spacing: 1px;
    color: var(--brand-blue);
  }
  .tagline {
    position: absolute;
    left: 134px;
    top: 168px;
    font-family: "Marcellus", serif;
    font-size: 15px;
    letter-spacing: 1.5px;
    text-transform: uppercase;
    color: var(--accent-orange);
  }
  .holder {
    position: absolute;
    right: 60px;
    top: 236px;
    text-align: left;
    font-family: "Noticia Text", serif;
  }
  .holder-name {
    font-size: 26px;
    font-weight: 700;
    color: var(--brand-blue);
    letter-spacing: 0.5px;
  }
  .holder-title {
    margin-left: 40px;
    font-size: 21px;
    font-weight: 700;
    color: var(--accent-orange);
  }

  /* Back */
  .card-back {
    top: 512px;
    background: var(--card-white);
  }
  .services-heading {
    position: absolute;
    left: 150px;
    top: 26px;
    font-family: "Noticia Text", serif;
    font-style: italic;
    font-size: 24px;
    color: var(--accent-orange);
    padding-bottom: 2px;
    border-bottom: 2px solid var(--divider);
  }
  .services {
    position: absolute;
    left: 0;
    top: 70px;
    list-style: none;
  }
  .service {
    width: 290px;
    height: 30px;
    margin-bottom: 8px;
    padding-left: 24px;
    background: var(--service-green);
    border-radius: 0 16px 16px 0;
    font-family: "Noticia Text", serif;
    font-style: italic;
    font-size: 17px;
    line-height: 30px;
    color: #ffffff;
  }
  .divider {
    position: absolute;
    left: 318px;
    top: 52px;
    width: 2px;
    height: 262px;
    background: var(--divider);
  }
  .contact {
    position: absolute;
    left: 344px;
    top: 62px;
    width: 284px;
    font-family: "Noticia Text", serif;
    font-size: 15px;
    line-height: 1.4;
    color: var(--contact-blue);
  }
  .contact .address { font-weight: 700; margin-bottom: 16px; }
  .contact p { margin-bottom: 14px; font-size: 16px; }
</style>
</head>
<body>
<main class="sheet">
  <section class="card card-front" aria-label="Card front">
    <div class="brand">
      <span class="brand-mark"></span>
      <span class="brand-name">Form Crafters</span>
    </div>
    <div class="tagline">We honour your natural form</div>
    <div class="holder">
      <div class="holder-name">Talvan Desoruthy</div>
      <div class="holder-title">Chief Executive</div>
    </div>
  </section>

  <section class="card card-back" aria-label="Card back">
    <h2 class="services-heading">services</h2>
    <ul class="services">
      <li class="service">Hair Restoration surgery</li>
      <li class="service">Hair Loss treatments</li>
      <li class="service">Breast surgery</li>
      <li class="service">Rhinoplasty</li>
      <li class="service">Zelix Liposuction</li>
      <li class="service">Fat Grafting</li>
      <li class="service">Lumex &amp; Fillers</li>
    </ul>
    <div class="divider"></div>
    <div class="contact">
      <div class="address">The London Calder Infirmary | 14 Pellmont Street | London | W1K 3TR Off Dunmore Lane</div>
      <p>Phone: +44 (0)207 146 5327</p>
      <p>Mobile: +44 (0)7491 825 436</p>
      <p>talvan@formcrafters-example.co.uk</p>
      <p>www.formcrafters-example.co.uk</p>
    </div>
  </section>
</main>
</body>
</html>
```